I need a business card for ALVA Holdings. We are a young startup based in New Zealand working in internet marketing and web development. The design should have some element connected to New Zealand, such as wave, koru or silver fern, just don't use a kiwi bird.

```html
<!DOCTYPE html>
<html lang="en">
<head>
<meta charset="utf-8">
<title>ALVA Holdings – Business Card</title>
<link rel="stylesheet" href="https://fonts.googleapis.com/css2?family=Jost:wght@400;500;600&display=swap">
<style>
  :root {
    --stage: #d9d4cd;
    --blue-light: #2467b8;
    --blue-deep: #0b3682;
    --frost-light: #f1f3f5;
    --frost-mid: #d6dce2;
    --wave-red: #d4301f;
    --wave-white: #ffffff;
    --swell: rgba(255,255,255,0.22);
    --ink-light: #f4f6fa;
    --brand-navy: #17336f;
    --brand-red: #c9321f;
  }
  html, body {
    margin: 0;
    width: 1200px;
    height: 969px;
    overflow: hidden;
    background: var(--stage);
  }
  .card {
    position: absolute;
    left: 120px;
    top: 212px;
    width: 960px;
    height: 545px;
    border-radius: 26px;
    overflow: hidden;
    background: linear-gradient(160deg, var(--frost-light) 0%, var(--frost-mid) 100%);
    box-shadow: 0 18px 40px rgba(0,0,0,0.18);
    font-family: "Jost", sans-serif;
  }
  .card-wave {
    position: absolute;
    inset: 0;
  }
  .brand {
    position: absolute;
    left: 520px;
    top: 58px;
    width: 350px;
    text-align: center;
    font-weight: 600;
    line-height: 1;
  }
  .brand-primary {
    display: block;
    font-size: 112px;
    letter-spacing: 4px;
    color: var(--brand-navy);
  }
  .brand-secondary {
    display: block;
    font-size: 38px;
    letter-spacing: 11px;
    margin-top: 8px;
    color: var(--brand-navy);
  }
  .holder {
    position: absolute;
    left: 62px;
    top: 200px;
    color: var(--ink-light);
  }
  .holder-name {
    margin: 0;
    font-size: 36px;
    font-weight: 500;
    letter-spacing: 1px;
    line-height: 1.1;
  }
  .holder-role {
    margin: 2px 0 0;
    font-size: 24px;
    font-weight: 400;
    letter-spacing: 0.5px;
  }
  .address {
    position: absolute;
    left: 62px;
    top: 300px;
    margin: 0;
    font-style: normal;
    font-size: 22px;
    line-height: 30px;
    color: var(--ink-light);
  }
  .contacts {
    position: absolute;
    left: 62px;
    top: 372px;
    margin: 0;
    padding: 0;
    list-style: none;
    font-size: 21px;
    line-height: 31px;
    color: var(--ink-light);
  }
  .contacts li {
    display: flex;
    align-items: center;
    gap: 14px;
  }
  .contacts svg {
    width: 20px;
    height: 20px;
    fill: var(--ink-light);
  }
</style>
</head>
<body>
  <div class="card">
    <svg class="card-wave" viewBox="0 0 960 545" preserveAspectRatio="none" aria-hidden="true">
      <defs>
        <linearGradient id="blueField" x1="0" y1="0" x2="1" y2="1">
          <stop offset="0" stop-color="var(--blue-light)"/>
          <stop offset="1" stop-color="var(--blue-deep)"/>
        </linearGradient>
      </defs>
      <path d="M0 0 H330 C400 170 560 440 915 545 H0 Z" fill="url(#blueField)"/>
      <g class="ocean-swell" fill="none" stroke="var(--swell)" stroke-width="2">
        <path d="M300 0 C370 175 520 420 850 545"/>
        <path d="M262 0 C330 185 470 420 760 545"/>
        <path d="M470 545 C540 500 600 470 660 500 C700 520 720 540 740 545"/>
        <path d="M540 545 C610 485 680 455 740 490 C770 510 790 530 805 545"/>
      </g>
      <path d="M334 8 C410 190 570 452 912 540" fill="none" stroke="var(--wave-white)" stroke-width="4"/>
      <path d="M345 30 C430 220 600 470 920 525" fill="none" stroke="var(--wave-red)" stroke-width="5"/>
    </svg>

    <div class="brand">
      <span class="brand-primary">ALVA</span>
      <span class="brand-secondary">HOLDINGS</span>
    </div>

    <div class="holder">
      <h1 class="holder-name">MAREN COLE</h1>
      <p class="holder-role">CEO/FOUNDER</p>
    </div>

    <address class="address">
      42 Harbour View Road<br>
      Wellington, New Zealand 6011
    </address>

    <ul class="contacts">
      <li>
        <svg viewBox="0 0 24 24"><path d="M6.6 10.8a15.1 15.1 0 0 0 6.6 6.6l2.2-2.2c.3-.3.7-.4 1-.2 1.1.4 2.3.6 3.6.6.6 0 1 .4 1 1V20c0 .6-.4 1-1 1A17 17 0 0 1 3 4c0-.6.4-1 1-1h3.5c.6 0 1 .4 1 1 0 1.3.2 2.5.6 3.6.1.3 0 .7-.2 1z"/></svg>
        021 555 0148
      </li>
      <li>
        <svg viewBox="0 0 24 24"><path d="M8 1h8a2 2 0 0 1 2 2v18a2 2 0 0 1-2 2H8a2 2 0 0 1-2-2V3a2 2 0 0 1 2-2zm0 3v14h8V4zm4 15.5a1 1 0 1 0 0 2 1 1 0 0 0 0-2z"/></svg>
        04 555 0192
      </li>
      <li>
        <svg viewBox="0 0 24 24"><path d="M2 5h20v14H2zm2 2v.4l8 5.2 8-5.2V7zm0 2.8V17h16V9.8l-8 5.2z"/></svg>
        maren@alvaholdings.co
      </li>
      <li>
        <svg viewBox="0 0 24 24"><path d="M12 2a10 10 0 1 0 0 20 10 10 0 0 0 0-20zm-1 17.9A8 8 0 0 1 4.2 10l4.8 4.8v1a2 2 0 0 0 2 2zm6.9-2.5a2 2 0 0 0-1.9-1.4h-1v-3a1 1 0 0 0-1-1H8v-2h2a1 1 0 0 0 1-1V7h2a2 2 0 0 0 2-2v-.4a8 8 0 0 1 2.9 12.8z"/></svg>
        www.alvaholdings.co
      </li>
    </ul>
  </div>
</body>
</html>
```